Modern and Clean Web Re-Design Project

We have 2 companies in similar industries: Printing and Mail Preparation/Fulfillment. We prefer sites that are clean and easy to navigate.Our printing company, Harbourline Press Works' website, hpwdirect.example is outdated needs revamping. We have rebranded our logo and are looking for a new design that is clean, modern and geared to other corporations and business in the downtown Toronto area. Our mailing company, The Postwick Depot (thepostwickdepot.example) needs a website as well. This company is in the Direct Mail and letter shop business, which essentially is addressing/personalizing people's printed matter and preparing it for either the Canadian or US postal service. The Postwick Depot specializes in not-for-profit and corporate sectors.Please see our logos to get an idea of the colors and look we want. For all intensive purposes, the sites can look similar in design all we want is that each site has the appropriate corporate colors and is a bit different so they don't look identical as the two business run as separate corporations.The content of the website should be easily changed by our staff and we want it to be setup to optimized for SEO based on the keywords we want. We are looking for someone to work on this project immediately
Updates

Project Deadline Extended
Reason: Change of ideas

After doing some thinking, I would like the site to be more modern but the non flash sites that I have seen so far Im finding life-less and while I want something clean, not overly busy and corporate looking, I dont want the design to be bland looking.

Please design with the previous specs in mind but with a twist as mentioned above.

Thanks
Dorian

Target Market(s)

See above

Industry/Entity Type

Printing

Requirements
Must have
• Must match the design and style of each respective logoSee the attached impage of the front of our offices to have an idea of our lookWe must be able to edit the content ourselves without any fancy programs or tools.Must be SEO optimized
Nice to have
• An online order form that can be emailed to us for quotes.....perhaps a page with a bunch of fields that have drop down menus....
Should not have
• Should not be overly busy. I want it to be clean and simple but informative without being hard to navigate

```html
<!DOCTYPE html>
<html lang="en">
<head>
<meta charset="utf-8">
<title>Harbourline Press Works</title>
<link rel="stylesheet" href="https://fonts.googleapis.com/css2?family=Arimo:wght@400;700&display=swap">
<style>
:root{
  --charcoal:#262425;
  --black:#111111;
  --orange-red:#f05133;
  --red:#e8452c;
  --amber:#f7a723;
  --ink:#333333;
  --muted:#8a8a8a;
  --footer-text:#a9a9a9;
  --field:#f7f7f7;
  --field-line:#e2e2e2;
  --white:#ffffff;
}
*{box-sizing:border-box;margin:0;padding:0}
html,body{width:1032px;height:1200px;overflow:hidden;background:var(--white)}
body{font-family:"Arimo",Arial,sans-serif}
.page{position:relative;width:1200px;height:1395px;transform:scale(.86);transform-origin:0 0}
.abs{position:absolute}

/* header */
.site-header{left:0;top:0;width:1200px;height:111px;background:var(--charcoal)}
.brand{left:130px;top:34px;display:flex;align-items:center;gap:10px;color:var(--amber);font-size:19px;font-weight:700;letter-spacing:.3px}
.brand-dot{width:22px;height:22px;border-radius:50%;background:var(--orange-red)}
.phone{left:930px;top:15px;display:flex;align-items:center;gap:10px;color:var(--white);font-size:18px}
.phone-icon{width:24px;height:24px;background:var(--orange-red);border-radius:3px;display:flex;align-items:center;justify-content:center}
.main-nav{right:119px;top:73px;display:flex;gap:42px}
.main-nav a{color:var(--white);text-decoration:none;font-size:14px}

/* slider */
.slider{left:120px;top:162px;width:959px;height:389px;border:1px solid #e4e4e4;overflow:hidden}
.slide-photo{position:absolute;inset:0;background:linear-gradient(90deg,#e9e4df 0%,#d9d2cb 30%,#e7ecef 55%,#dfe6ea 80%,#cfd6dc 100%)}
.slide-title{position:absolute;left:509px;top:74px;font-size:49px;font-weight:700;color:var(--amber);letter-spacing:.5px}
.slide-tag{position:absolute;left:510px;top:131px;background:var(--red);color:var(--white);font-weight:700;font-size:18px;padding:3px 8px;letter-spacing:.4px}
.slide-points{position:absolute;left:510px;top:202px;list-style:none}
.slide-points li{display:flex;align-items:center;gap:17px;height:50px;font-size:18px;color:var(--ink)}
.tick{width:32px;height:32px;border-radius:50%;background:var(--amber);display:flex;align-items:center;justify-content:center}
.slider-arrow{width:30px;height:30px;border-radius:50%;background:#6b6b6b;display:flex;align-items:center;justify-content:center}

/* services band */
.services{left:0;top:551px;width:1200px;height:208px;background:var(--orange-red)}
.service{position:absolute;top:12px;width:230px;text-align:center;color:var(--white)}
.service svg{display:block;margin:0 auto;height:72px}
.service h3{font-weight:400;font-size:20px;margin-top:16px}
.service p{font-size:12px;line-height:16px;letter-spacing:.6px;margin-top:8px}

/* about */
.section-title{font-size:18px;font-weight:700;color:var(--ink);letter-spacing:.3px}
.about-photo{left:120px;top:834px;width:206px;height:105px;border:3px solid #f1f1f1;background:linear-gradient(90deg,#c9d6e2,#eef2f5 45%,#e8d7c8)}
.about-text{font-size:12px;line-height:16px;color:var(--muted);text-align:justify;letter-spacing:.2px}

/* quote form */
.field{left:809px;width:271px;background:var(--field);border:2px solid var(--field-line);color:#777;font-size:14px;padding:9px 10px;letter-spacing:.4px}
.send-btn{left:962px;top:1039px;width:118px;height:32px;background:var(--red);color:var(--white);font-size:14px;display:flex;align-items:center;justify-content:center}

/* footer */
.site-footer{left:4px;top:1135px;width:1196px;height:214px;background:var(--charcoal)}
.footer-title{color:var(--white);font-size:14px}
.footer-list{list-style:none}
.footer-list li{font-size:12px;color:var(--footer-text);height:24px;letter-spacing:.5px}
.contact-line{display:flex;gap:10px;font-size:12px;line-height:14px;color:var(--footer-text);letter-spacing:.6px}
.contact-line svg{flex:none;margin-top:1px}
.newsletter-text{font-size:12px;line-height:14px;color:var(--footer-text);text-align:justify;letter-spacing:.3px}
.newsletter-form{left:860px;top:1245px;width:220px;height:33px;display:flex}
.newsletter-input{flex:1;background:var(--white);font-size:13px;color:#555;padding:9px 9px;letter-spacing:.5px}
.newsletter-btn{width:59px;background:var(--amber);color:var(--white);font-size:14px;display:flex;align-items:center;justify-content:center}
.bottom-bar{left:4px;top:1349px;width:1196px;height:46px;background:var(--black)}
.copyright{left:120px;top:1364px;color:var(--white);font-size:12px;letter-spacing:.4px}
.social{width:24px;height:24px;background:#6a6a6a;top:1359px}
</style>
</head>
<body>
<div class="page">

  <header class="site-header abs">
    <div class="brand abs"><span class="brand-dot"></span>Harbourline Press Works</div>
    <div class="phone abs">
      <span class="phone-icon"><svg width="14" height="14" viewBox="0 0 14 14"><path d="M3 1l2 3-1 1.5c.8 1.7 2 2.9 3.5 3.5L9 8l3 2-1 2.5C6 12 2 8 1.5 2z" fill="#fff"/></svg></span>
      416-555-0147
    </div>
    <nav class="main-nav abs">
      <a href="#">Home</a><a href="#">About Us</a><a href="#">Our Services</a><a href="#">News</a><a href="#">Contact Us</a>
    </nav>
  </header>

  <div class="slider-arrow abs" style="left:31px;top:348px"><svg width="16" height="12" viewBox="0 0 16 12"><path d="M15 6H2M6 1L1 6l5 5" stroke="#fff" stroke-width="1.5" fill="none"/></svg></div>
  <div class="slider-arrow abs" style="left:1136px;top:348px"><svg width="16" height="12" viewBox="0 0 16 12"><path d="M1 6h13M10 1l5 5-5 5" stroke="#fff" stroke-width="1.5" fill="none"/></svg></div>

  <section class="slider abs">
    <div class="slide-photo" role="img" aria-label="Photo of a smiling businesswoman in a bright office with colleagues blurred behind"></div>
    <h1 class="slide-title">Digital Printing</h1>
    <div class="slide-tag">Smart Solutions for your Business</div>
    <ul class="slide-points">
      <li><span class="tick"><svg width="16" height="14" viewBox="0 0 16 14"><path d="M2 7l4 4 8-9" stroke="#fff" stroke-width="3" fill="none"/></svg></span>Lorem ipsum dolor sit amet.</li>
      <li><span class="tick"><svg width="16" height="14" viewBox="0 0 16 14"><path d="M2 7l4 4 8-9" stroke="#fff" stroke-width="3" fill="none"/></svg></span>Nulla at quam arcu, eu dapibus ipsum.</li>
      <li><span class="tick"><svg width="16" height="14" viewBox="0 0 16 14"><path d="M2 7l4 4 8-9" stroke="#fff" stroke-width="3" fill="none"/></svg></span>Sed ac tellus at urna dignissim congue.</li>
    </ul>
  </section>

  <section class="services abs">
    <div class="service" style="left:114px">
      <svg viewBox="0 0 100 72" width="100"><rect x="4" y="16" width="34" height="44" rx="3" fill="none" stroke="#fff" stroke-width="4"/><rect x="62" y="16" width="34" height="44" rx="3" fill="none" stroke="#fff" stroke-width="4"/><path d="M11 28h20M11 36h20M11 44h20M69 28h20M69 36h20M69 44h20" stroke="#fff" stroke-width="3"/><path d="M42 32h8v-8l12 14-12 14v-8h-8z" fill="#fff"/></svg>
      <h3>Legal Copy</h3>
      <p>Lorem ipsum dolor sit amet, con-<br>sectetur adipiscing elit. Nunc eget<br>magna enim.</p>
    </div>
    <div class="service" style="left:362px">
      <svg viewBox="0 0 80 72" width="80"><rect x="20" y="4" width="40" height="22" rx="3" fill="#fff"/><rect x="4" y="24" width="72" height="34" rx="5" fill="#fff"/><rect x="18" y="50" width="44" height="18" fill="#fff" stroke="#f05133" stroke-width="3"/><path d="M24 57h32M24 62h32" stroke="#f05133" stroke-width="2"/><circle cx="66" cy="34" r="3" fill="#f05133"/></svg>
      <h3>Digital Printing</h3>
      <p>Lorem ipsum dolor sit amet, con-<br>sectetur adipiscing elit. Nunc eget<br>magna enim.</p>
    </div>
    <div class="service" style="left:608px">
      <svg viewBox="0 0 70 72" width="70"><path d="M16 18c0-10 12-14 30-14 12 0 20 4 20 12 0 6-6 10-12 10l-12 36c-4 8-14 10-22 6-8-4-10-14-4-20z" fill="#fff"/><circle cx="22" cy="54" r="6" fill="#f05133"/><path d="M24 22l28-8M22 30l26-6" stroke="#f05133" stroke-width="3"/></svg>
      <h3>Offset Printing</h3>
      <p>Lorem ipsum dolor sit amet, con-<br>sectetur adipiscing elit. Nunc eget<br>magna enim.</p>
    </div>
    <div class="service" style="left:854px">
      <svg viewBox="0 0 84 72" width="84"><path d="M4 28L42 4l38 24v40H4z" fill="#fff"/><path d="M4 68l30-24M80 68L50 44" stroke="#f05133" stroke-width="3"/><rect x="30" y="20" width="24" height="16" fill="#f05133"/><path d="M34 26h16M34 31h16" stroke="#fff" stroke-width="2"/></svg>
      <h3>Mailing</h3>
      <p>Lorem ipsum dolor sit amet, con-<br>sectetur adipiscing elit. Nunc eget<br>magna enim.</p>
    </div>
  </section>

  <h2 class="section-title abs" style="left:120px;top:798px">Who We Are</h2>
  <div class="about-photo abs" role="img" aria-label="Photo of a cheering office team with a smiling woman giving a thumbs up"></div>
  <p class="about-text abs" style="left:340px;top:832px;width:385px">Lorem ipsum dolor sit amet, consectetur adipiscing elit. Nunc eget magna enim. Morbi at tortor enim, quis gravida lacus. Phasellus tempor lorem nec ipsum adipiscing mattis. Integer placerat dictum eros, vitae pulvinar neque vestibulum et. Proin imperdiet, felis vel consectetur ornare, dui leo pulvinar erat, eu dictum justo nibh vel quam. Mauris interdum vehicula enim, eu aliquet tortor volutpat sit amet. Fusce nec augue metus.</p>
  <p class="about-text abs" style="left:120px;top:957px;width:605px">Morbi dui nisi, luctus ut faucibus ut, pellentesque nec metus. Curabitur consectetur, eros ac convallis ele-mentum, neque nunc molestie leo, eu accumsan erat nisi sit amet quam. Quisque ac eros odio. Aliquam hendrerit pulvinar elit, at blandit tortor tincidunt non. Praesent ultricies enim est, in blandit sem. Nam tincid-unt ipsum et eros tempus a sodales tortor sagittis. Ut ut dolor mauris. Quisque sed magna neque. Maecenas vel condimentum dolor.</p>

  <h2 class="section-title abs" style="left:808px;top:798px">Get a Free Quote</h2>
  <div class="field abs" style="top:835px;height:37px">Name</div>
  <div class="field abs" style="top:887px;height:37px">Email</div>
  <div class="field abs" style="top:938px;height:88px">Write a message</div>
  <div class="send-btn abs">Send Message</div>

  <footer class="site-footer abs"></footer>
  <h4 class="footer-title abs" style="left:120px;top:1155px">Navigation</h4>
  <ul class="footer-list abs" style="left:122px;top:1190px"><li>Home</li><li>About Us</li><li>Our Services</li><li>News</li><li>Contact Us</li></ul>
  <h4 class="footer-title abs" style="left:348px;top:1155px">Our Services</h4>
  <ul class="footer-list abs" style="left:350px;top:1190px"><li>Suspendisse</li><li>Nullam fermentum</li><li>Integer ornare</li><li>Proin iaculis</li><li>Praesent ac</li></ul>
  <h4 class="footer-title abs" style="left:575px;top:1155px">Contact us</h4>
  <div class="contact-line abs" style="left:577px;top:1190px"><svg width="10" height="14" viewBox="0 0 10 14"><path d="M5 0a5 5 0 0 1 5 5c0 4-5 9-5 9S0 9 0 5a5 5 0 0 1 5-5z" fill="#888"/><circle cx="5" cy="5" r="2" fill="#262425"/></svg><span>48 Quayside Ave Concourse<br>Level Toronto, On M5V 0Z9</span></div>
  <div class="contact-line abs" style="left:577px;top:1238px"><svg width="11" height="12" viewBox="0 0 14 14"><path d="M3 1l2 3-1 1.5c.8 1.7 2 2.9 3.5 3.5L9 8l3 2-1 2.5C6 12 2 8 1.5 2z" fill="#888"/></svg><span>416-555-0147</span></div>
  <div class="contact-line abs" style="left:577px;top:1268px"><svg width="12" height="10" viewBox="0 0 12 10"><rect width="12" height="10" fill="#888"/><path d="M0 0l6 5 6-5" stroke="#262425" fill="none"/></svg><span>mara@hpwdirect.example</span></div>
  <h4 class="footer-title abs" style="left:860px;top:1155px">Newsletter</h4>
  <p class="newsletter-text abs" style="left:860px;top:1190px;width:220px">Lorem ipsum dolor sit amet, consecte-tur adipiscing elit. Nunc eget magna enim.</p>
  <div class="newsletter-form abs"><div class="newsletter-input">Email Address</div><div class="newsletter-btn">Submit</div></div>

  <div class="bottom-bar abs"></div>
  <div class="copyright abs">Copyright © 2013 HPW. All Right Reserved.</div>
  <span class="social abs" style="left:980px"></span>
  <span class="social abs" style="left:1018px"></span>
  <span class="social abs" style="left:1056px"></span>
</div>
</body>
</html>
```